We are needed to get an artwork developed for a conference booth across 2 background panels. The design we’d like is of the tree from our existing Lanternfield Studio logo (included). Not wanting a black background.
In addition we’d like the title text
COMMUNITY RECOVERY
COMMUNITY RESILIENCE
A set of national principles
A community of practice
How can we shape the future together?

We are also wanting to have the following text in the roots of the tree.
- Understand the context
- Recognise complexity
- Use community-led approaches
- Coordinate all activities
- Communicate effectively
- Recognise and build capacity

Important – Artwork Requirements
Create 2 conference Digital Print Panels 985mmW x 2347mmH. The conference panels will be put together with a 5mm gap avoid small text in this area.
Print-ready artwork files are to be scaled at correct dimensions.
All artwork must be submitted no larger than 50% scale. Do not supply artwork files over 300MB for large images – Scaling to 50% @ 300 DPI is preferred.
No bleed required for panel prints.
All fonts must be outlined.
Overprint to be turned OFF.
Flatten all transparencies.
Supply as one single layer.
Embed all links.
PDF file submission
Please supply artwork to the exact specifications (dimension, text and images) and high resolution print-ready files.

```html
<!DOCTYPE html>
<html lang="en">
<head>
<meta charset="utf-8">
<title>Community Recovery Community Resilience – Booth Panels</title>
<link href="https://fonts.googleapis.com/css2?family=Saira:wght@300;400;500;600;700&display=swap" rel="stylesheet">
<style>
  :root{
    --stage:#354451;
    --sky:#74b2e6;
    --root-band:#134f9e;
    --ground:#077dd8;
    --white:#ffffff;
    --tree-glow:#a9d0f1;
  }
  *{margin:0;padding:0;box-sizing:border-box}
  html,body{width:1200px;height:1200px;overflow:hidden;background:var(--stage)}
  body{font-family:"Saira",sans-serif;color:var(--white);position:relative}
  .panel{position:absolute;top:122px;width:401px;height:954px;background:var(--sky);overflow:hidden}
  .panel--left{left:199px}
  .panel--right{left:605px}
  .bands{position:absolute;left:0;top:0;width:401px;height:954px}
  .tree-art{position:absolute;top:0;left:0;width:401px;height:954px}
  .title{position:absolute;left:46px;top:42px;font-size:50px;line-height:50px;letter-spacing:0.5px}
  .title span{display:block}
  .title .light{font-weight:300}
  .title .bold{font-weight:700}
  .tagline{position:absolute;font-size:25px;font-weight:500;line-height:1}
  .tagline--principles{left:48px;top:522px}
  .tagline--practice{left:58px;top:522px}
  .question{position:absolute;left:62px;top:108px;font-size:25px;font-weight:500;line-height:32px}
  .question span{display:block}
  .question .indent{padding-left:31px}
  .roots{position:absolute;top:718px;display:flex;align-items:stretch}
  .panel--left .roots{left:48px}
  .panel--right .roots{left:56px}
  .root{font-size:13.5px;font-weight:500;line-height:16.5px;padding:0 12px;border-left:1px solid rgba(255,255,255,0.45)}
  .root:first-child{padding-left:0;border-left:none}
  .studio{position:absolute;left:74px;top:830px;display:flex;align-items:center;gap:14px}
  .studio-dot{width:40px;height:40px;border-radius:50%;border:1.5px solid var(--white)}
  .studio-name{font-size:26px;font-weight:500;line-height:1}
  .studio-sub{font-size:11px;font-weight:300;margin-top:4px}
  .partners{position:absolute;left:46px;top:830px;display:flex;align-items:center}
  .partner{display:flex;align-items:center;gap:8px}
  .partner--institute .partner-name{text-align:right;font-size:10.5px;line-height:12px;font-weight:400}
  .partner-mark{width:40px;height:40px;border-radius:50%;background:var(--white)}
  .partner-mark--ring{background:none;border:1.5px solid var(--white)}
  .partner-divider{width:1px;height:36px;background:rgba(255,255,255,0.7);margin:0 16px}
  .partner--group .partner-name{font-size:7.5px;line-height:9.5px;font-weight:400}
  .partner--group .country{font-size:5.5px;letter-spacing:0.8px}
</style>
</head>
<body>

<section class="panel panel--left">
  <svg class="tree-art" viewBox="0 0 401 954" role="img" aria-label="White hand-drawn tree with leaves and flowing lines, trunk and roots reaching into the ground band; continues onto the right panel">
    <defs>
      <radialGradient id="glowLeft" cx="1" cy="0.55" r="0.75">
        <stop offset="0" stop-color="var(--tree-glow)" stop-opacity="0.85"/>
        <stop offset="1" stop-color="var(--tree-glow)" stop-opacity="0"/>
      </radialGradient>
    </defs>
    <rect x="120" y="250" width="281" height="600" fill="url(#glowLeft)"/>
  </svg>
  <svg class="bands" viewBox="0 0 401 954" aria-hidden="true">
    <path d="M0 684 C60 680 100 688 150 684 S260 688 300 684 S370 680 401 684 V792 H0 Z" fill="var(--root-band)"/>
    <path d="M0 788 C60 785 100 792 150 788 S260 792 300 788 S370 784 401 788 V954 H0 Z" fill="var(--ground)"/>
  </svg>
  <h1 class="title">
    <span class="light">COMMUNITY</span>
    <span class="bold">RECOVERY</span>
    <span class="light">COMMUNITY</span>
    <span class="bold">RESILIENCE</span>
  </h1>
  <p class="tagline tagline--principles">A set of national principles</p>
  <ul class="roots">
    <li class="root" style="list-style:none">Understand<br>the context</li>
    <li class="root" style="list-style:none">Recognise<br>complexity</li>
    <li class="root" style="list-style:none">Use community-led<br>approaches</li>
  </ul>
  <div class="studio">
    <div class="studio-dot"></div>
    <div>
      <div class="studio-name">Lanternfield Studio</div>
      <div class="studio-sub">Community recovery practitioners</div>
    </div>
  </div>
</section>

<section class="panel panel--right">
  <svg class="tree-art" viewBox="0 0 401 954" role="img" aria-label="Upper branches, leaves, trunk and roots of the white hand-drawn tree, with flowing lines sweeping to the right edge">
    <defs>
      <radialGradient id="glowRight" cx="0" cy="0.5" r="0.8">
        <stop offset="0" stop-color="var(--tree-glow)" stop-opacity="0.85"/>
        <stop offset="1" stop-color="var(--tree-glow)" stop-opacity="0"/>
      </radialGradient>
    </defs>
    <rect x="0" y="210" width="300" height="640" fill="url(#glowRight)"/>
  </svg>
  <svg class="bands" viewBox="0 0 401 954" aria-hidden="true">
    <path d="M0 684 C40 680 100 688 150 684 S260 688 300 684 S370 680 401 684 V792 H0 Z" fill="var(--root-band)"/>
    <path d="M0 788 C40 784 100 792 150 788 S260 792 300 788 S370 784 401 788 V954 H0 Z" fill="var(--ground)"/>
  </svg>
  <p class="question">
    <span>How can we shape</span>
    <span class="indent">the future together?</span>
  </p>
  <p class="tagline tagline--practice">A community of practice</p>
  <ul class="roots">
    <li class="root" style="list-style:none">Coordinate<br>all activities</li>
    <li class="root" style="list-style:none">Communicate<br>effectively</li>
    <li class="root" style="list-style:none">Recognise and<br>build capacity</li>
  </ul>
  <div class="partners">
    <div class="partner partner--institute">
      <div class="partner-name">Coastline Institute for<br>Hazard Preparedness</div>
      <div class="partner-mark"></div>
    </div>
    <div class="partner-divider"></div>
    <div class="partner partner--group">
      <div class="partner-mark partner-mark--ring"></div>
      <div class="partner-name">Civic Renewal<br>Reference Group<br><span class="country">AUSTRALIA</span></div>
    </div>
  </div>
</section>

</body>
</html>
```